Chimney Service company needs new business card design

We need a updated business card with our new logo added. We provide a full range of chimney services throughout Vermont and New Hampshire. The business card will be one sided and color. Attached is our current business card another document showing all the information we would like on the card.
We dont like a lot of flashy colors.... here is a link to our website to get an idea of our branding www.flueguardnorthvt-example.com

Target Market(s)

homeowners

Industry/Entity Type

Business

Contact Information for Business Card

See attached sheet for content.

Font styles to use
Serif
Sans Serif

Requirements
Must have
• all information provided on separate sheet
Should not have
• Additional information that may clogg up design

```html
<!DOCTYPE html>
<html lang="en">
<head>
<meta charset="utf-8">
<title>Flueguard North – Business Card</title>
<link href="https://fonts.googleapis.com/css2?family=Cinzel:wght@500&family=Lato:wght@400;700&display=swap" rel="stylesheet">
<style>
  :root {
    --stage: #e6e4e2;
    --paper: #ffffff;
    --brand-red: #b00000;
    --ink: #333333;
    --ink-soft: #555555;
    --rule: #b5b5b5;
    --on-red: #ffffff;
  }
  * { box-sizing: border-box; margin: 0; padding: 0; }
  html, body { width: 1200px; height: 844px; overflow: hidden; }
  body {
    background: var(--stage);
    font-family: "Lato", Arial, sans-serif;
    position: relative;
  }
  .card {
    position: absolute;
    width: 525px;
    height: 300px;
    top: 272px;
    box-shadow: 0 6px 18px rgba(0,0,0,0.18);
    overflow: hidden;
  }
  .card--front { left: 60px; background: var(--paper); color: var(--ink); }
  .card--back { left: 615px; background: var(--brand-red); color: var(--on-red); }

  /* Front */
  .brand {
    position: absolute;
    top: 34px;
    right: 40px;
    display: flex;
    align-items: center;
    gap: 12px;
  }
  .brand__mark {
    width: 40px;
    height: 40px;
    border: 5px solid var(--ink);
  }
  .brand__name {
    font-family: "Cinzel", Georgia, serif;
    font-weight: 500;
    font-size: 27px;
    letter-spacing: 1px;
    color: var(--ink);
    text-transform: uppercase;
    white-space: nowrap;
  }
  .tagline {
    position: absolute;
    top: 92px;
    right: 40px;
    font-size: 13px;
    color: var(--brand-red);
    letter-spacing: 0.2px;
    text-transform: uppercase;
    white-space: nowrap;
  }
  .rule {
    position: absolute;
    height: 1px;
    background: var(--rule);
  }
  .rule--top { top: 116px; left: 150px; right: 40px; }
  .rule--mid { top: 206px; left: 36px; right: 250px; }

  .contact {
    position: absolute;
    top: 142px;
    left: 36px;
    right: 40px;
    font-size: 14px;
    line-height: 22px;
    white-space: nowrap;
  }
  .contact__label { color: var(--brand-red); font-weight: 700; margin-right: 4px; }
  .contact__web {
    position: absolute;
    top: 0;
    right: 0;
    color: var(--brand-red);
    font-size: 13px;
  }

  .services {
    position: absolute;
    top: 218px;
    left: 36px;
    right: 30px;
    display: grid;
    grid-template-columns: 190px 1fr;
    row-gap: 4px;
    list-style: none;
    font-size: 14px;
    line-height: 18px;
    color: var(--ink-soft);
  }
  .services li { display: flex; align-items: center; gap: 7px; white-space: nowrap; }
  .services li::before {
    content: "";
    width: 7px;
    height: 7px;
    background: var(--brand-red);
    flex: none;
  }

  /* Back */
  .back__name {
    position: absolute;
    top: 110px;
    left: 0;
    right: 0;
    text-align: center;
    font-family: "Cinzel", Georgia, serif;
    font-weight: 500;
    font-size: 34px;
    letter-spacing: 1.5px;
    text-transform: uppercase;
    white-space: nowrap;
  }
  .back__web {
    position: absolute;
    bottom: 36px;
    right: 40px;
    font-size: 13px;
    font-weight: 700;
    white-space: nowrap;
  }
</style>
</head>
<body>
  <section class="card card--front" aria-label="Business card front">
    <div class="brand">
      <span class="brand__mark"></span>
      <span class="brand__name">Flueguard North</span>
    </div>
    <p class="tagline">Serving VT and New Hampshire since 1989</p>
    <div class="rule rule--top"></div>

    <div class="contact">
      <p><span class="contact__label">P:</span>802-555-0142</p>
      <p><span class="contact__label">E:</span>info@flueguardnorthvt-example.com</p>
      <span class="contact__web">www.flueguardnorthvt-example.com</span>
    </div>
    <div class="rule rule--mid"></div>

    <ul class="services">
      <li>Full Masonry Services</li>
      <li>Historic chimney restoration</li>
      <li>Stainless steel liners</li>
      <li>New Chimney installations</li>
      <li>Guild Certified Chimney sweeps</li>
    </ul>
  </section>

  <section class="card card--back" aria-label="Business card back">
    <p class="back__name">Flueguard North</p>
    <p class="back__web">www.flueguardnorthvt-example.com</p>
  </section>
</body>
</html>
```